Design NEW business card

We would like a business card using the colour deep red wine or dark navy blue textured background (patterned or not, open to suggestions) with a high gloss debossed rose gold/copper TM Thomas Marlow Jewellery business name (Provided). I have included images for your review we would like to keep our currently logo and business name on the front but you can change the layout and positioning. For the back of the card we are open to all suggestions/variations.
Use our current TM Thomas Marlow Jewellery logo (Provided image)

```html
<!DOCTYPE html>
<html lang="en">
<head>
<meta charset="utf-8">
<title>Thomas Marlow Jewellery – Business Card</title>
<link href="https://fonts.googleapis.com/css2?family=Open+Sans:wght@400;600&display=swap" rel="stylesheet">
<style>
  :root {
    --stage: #2b2623;
    --wine: #6b2a31;
    --wine-deep: #5a2128;
    --ink-light: #ffffff;
    --rose-gold: #c8936e;
    --silver: #d8d6d4;
  }
  * { margin: 0; padding: 0; box-sizing: border-box; }
  html, body {
    width: 1200px; height: 900px; overflow: hidden;
    background: var(--stage);
    font-family: "Open Sans", Arial, sans-serif;
  }
  .stage {
    width: 1200px; height: 900px;
    display: flex; align-items: center; justify-content: center; gap: 40px;
  }
  .card {
    position: relative;
    width: 540px; height: 309px;
    background: radial-gradient(ellipse at 40% 35%, var(--wine) 0%, var(--wine-deep) 100%);
    box-shadow: 0 10px 30px rgba(0,0,0,.45);
  }
  .brand {
    position: absolute;
    display: flex; align-items: center; gap: 12px;
    font-weight: 400; text-transform: uppercase;
    letter-spacing: .28em; line-height: 1.5;
  }
  .brand-dot {
    width: 14px; height: 14px; border-radius: 50%;
    flex: none;
  }
  .card-contact .brand {
    left: 40px; top: 132px; width: 230px;
    color: var(--rose-gold); font-size: 14px;
  }
  .card-contact .brand-dot { background: var(--rose-gold); }
  .card-logo .brand {
    left: 140px; top: 118px; width: 280px;
    color: var(--silver); font-size: 17px;
  }
  .card-logo .brand-dot { background: var(--silver); width: 16px; height: 16px; }
  .contact {
    position: absolute; left: 290px; top: 62px;
    color: var(--ink-light);
  }
  .contact-name { font-size: 22px; font-weight: 600; line-height: 1.2; }
  .contact-role { font-size: 13px; margin-bottom: 12px; }
  .contact-address { font-size: 13px; line-height: 1.4; margin-bottom: 8px; }
  .contact-list { list-style: none; font-size: 13px; line-height: 1.55; }
  .contact-list li { display: flex; align-items: center; gap: 9px; }
  .contact-list svg { width: 12px; height: 12px; flex: none; }
</style>
</head>
<body>
<main class="stage">
  <section class="card card-contact">
    <div class="brand"><span class="brand-dot"></span><span>TM Thomas Marlow Jewellery</span></div>
    <div class="contact">
      <p class="contact-name">Daniel Hart</p>
      <p class="contact-role">Managing Director</p>
      <p class="contact-address">48 Linden Row, Harbury<br>United Kingdom, HB4 2TM.</p>
      <ul class="contact-list">
        <li>
          <svg viewBox="0 0 12 12" aria-hidden="true"><path fill="#fff" d="M2.4 1l1.8 2.2-.9 1.2c.7 1.5 1.8 2.6 3.3 3.3l1.2-.9L10 8.6 9.3 10.6C5 10.4 1.6 7 1.4 2.7z"/></svg>
          044-987 654 321
        </li>
        <li>
          <svg viewBox="0 0 12 12" aria-hidden="true"><rect x="1" y="2.5" width="10" height="7" fill="#fff"/><path d="M1 2.5l5 4 5-4" fill="none" stroke="#6b2a31" stroke-width="1"/></svg>
          info@thomasmarlow.com
        </li>
        <li>
          <svg viewBox="0 0 12 12" aria-hidden="true"><g fill="none" stroke="#fff" stroke-width="1.3"><rect x="1.5" y="5" width="5" height="3" rx="1.5" transform="rotate(-45 4 6.5)"/><rect x="5.5" y="3.5" width="5" height="3" rx="1.5" transform="rotate(-45 8 5)"/></g></svg>
          www.thomasmarlow.com
        </li>
      </ul>
    </div>
  </section>

  <section class="card card-logo">
    <div class="brand"><span class="brand-dot"></span><span>TM Thomas Marlow Jewellery</span></div>
  </section>
</main>
</body>
</html>
```